KT Fenwick's Brochure - Brevanta Solutions

Hello,
We have an example of very simple brochure (attached below). We would like you to make it better. More sophisticated. More professional looking. All of the info in the document needs to go in the brochure.
Please let me know if you can execute. I will be happy to send over photos, logos etc, once I know.

```html
<!DOCTYPE html>
<html lang="en">
<head>
<meta charset="utf-8">
<title>KT Fenwick's – Brevanta Solutions Flyer Set</title>
<link href="https://fonts.googleapis.com/css2?family=Bebas+Neue&family=Montserrat:wght@400;500&display=swap" rel="stylesheet">
<style>
  :root{
    --page-bg:#b2b2b2;
    --brand-blue:#263b8c;
    --ink:#0e0e10;
    --body-ink:#1e2230;
    --sheet-light:#e6e8ee;
    --white:#ffffff;
    --muted:#5a5f6c;
  }
  *{box-sizing:border-box}
  html,body{margin:0;padding:0}
  body{width:1200px;height:1006px;overflow:hidden;background:var(--page-bg);position:relative;font-family:'Montserrat',sans-serif;color:var(--body-ink)}
  .flyer{position:absolute;width:278px;height:392px;overflow:hidden;box-shadow:3px 4px 6px rgba(0,0,0,.35);background:var(--sheet-light)}
  .flyer-art{position:absolute;inset:0;width:278px;height:392px}
  .brand-name{position:absolute;left:10px;top:10px;font-family:'Bebas Neue',sans-serif;font-size:10px;letter-spacing:.4px;color:var(--brand-blue);margin:0;line-height:1}
  .content{position:absolute;left:15px;right:12px}
  .title{font-family:'Bebas Neue',sans-serif;font-weight:400;font-size:39px;line-height:.9;color:var(--ink);margin:0}
  .title .accent{display:block;color:var(--brand-blue)}
  .title.compact .line{font-size:28px;display:block;line-height:.88}
  .subtitle{font-family:'Bebas Neue',sans-serif;font-size:19px;color:var(--brand-blue);margin:10px 0 0;line-height:1}
  .lead{font-size:7px;line-height:1.6;margin:10px 0 8px}
  .points{list-style:none;padding:0;margin:0 0 8px;display:grid;grid-template-columns:1fr 1fr;column-gap:8px;row-gap:6px;font-size:7px;line-height:1.6}
  .points li{position:relative;padding-left:7px}
  .points li::before{content:"";position:absolute;left:0;top:4px;width:2.5px;height:2.5px;border-radius:50%;background:var(--ink)}
  .points.tight{row-gap:1px}
  .tabs{display:grid;grid-template-columns:1fr 1fr;gap:18px;margin-top:2px}
  .tab-head{font-family:'Bebas Neue',sans-serif;font-weight:400;font-size:10.5px;color:var(--white);background:var(--brand-blue);padding:5px 8px 4px;margin:0 0 4px;clip-path:polygon(0 0,88% 0,100% 100%,0 100%);letter-spacing:.3px}
  .tab-list{list-style:none;padding:0 0 0 6px;margin:0;font-size:7px;line-height:1.6}
  .tab-list li{position:relative;padding-left:6px}
  .tab-list li::before{content:"";position:absolute;left:0;top:4px;width:2.5px;height:2.5px;border-radius:50%;background:var(--ink)}
  .contact-bar{position:absolute;left:16px;bottom:7px;display:flex;align-items:center;gap:4px;font-family:'Bebas Neue',sans-serif;font-size:11px;color:var(--white);letter-spacing:.2px}
  .contact-bar .divider{display:inline-block;width:1px;height:10px;background:var(--white);margin:0 2px}
  .web{position:absolute;left:167px;bottom:10px;font-size:5px;color:var(--muted)}
  .f1{left:131px;top:98px}.f2{left:443px;top:98px}.f3{left:751px;top:98px}
  .f4{left:131px;top:517px}.f5{left:443px;top:517px}.f6{left:751px;top:517px}
</style>
</head>
<body>

<svg width="0" height="0" style="position:absolute" aria-hidden="true">
  <defs>
    <linearGradient id="sheetTone" x1="0" y1="0" x2="0" y2="1">
      <stop offset="0" stop-color="#dfe3ec"/>
      <stop offset="1" stop-color="#c9c9ce"/>
    </linearGradient>
    <linearGradient id="skyTone" x1="0" y1="0" x2="1" y2="1">
      <stop offset="0" stop-color="#5f79a8"/>
      <stop offset="1" stop-color="#9fb0c8"/>
    </linearGradient>
    <linearGradient id="towerTone" x1="0" y1="0" x2="1" y2="1">
      <stop offset="0" stop-color="#2f4d86"/>
      <stop offset="1" stop-color="#6f8bb6"/>
    </linearGradient>
    <linearGradient id="brickTone" x1="0" y1="0" x2="1" y2="1">
      <stop offset="0" stop-color="#8a5a4d"/>
      <stop offset="1" stop-color="#7b8da6"/>
    </linearGradient>
    <linearGradient id="shopTone" x1="0" y1="0" x2="1" y2="1">
      <stop offset="0" stop-color="#4b4f55"/>
      <stop offset="1" stop-color="#8c8f94"/>
    </linearGradient>
    <linearGradient id="officeTone" x1="0" y1="0" x2="1" y2="1">
      <stop offset="0" stop-color="#c6cbd2"/>
      <stop offset="1" stop-color="#1f3b91"/>
    </linearGradient>
    <symbol id="sheetFrame" viewBox="0 0 485 686">
      <polygon points="137,175 220,112 485,290 485,400" fill="#263b8c"/>
      <polygon points="0,640 270,640 290,686 0,686" fill="#0e0e10"/>
      <polygon points="400,686 485,600 485,686" fill="#0e0e10"/>
    </symbol>
    <symbol id="phoneIcon" viewBox="0 0 24 24">
      <path fill="#fff" d="M6.6 10.8c1.4 2.8 3.8 5.1 6.6 6.6l2.2-2.2c.3-.3.7-.4 1-.2 1.1.4 2.3.6 3.6.6.6 0 1 .4 1 1V20c0 .6-.4 1-1 1C10.6 21 3 13.4 3 4c0-.6.4-1 1-1h3.5c.6 0 1 .4 1 1 0 1.3.2 2.5.6 3.6.1.3 0 .7-.2 1z"/>
    </symbol>
  </defs>
</svg>

<!-- Flyer 1 -->
<article class="flyer f1">
  <svg class="flyer-art" viewBox="0 0 485 686" preserveAspectRatio="none">
    <rect width="485" height="686" fill="url(#sheetTone)" role="img" aria-label="Faded city skyline behind the text"/>
    <polygon points="0,115 70,0 330,0 140,175 0,280" fill="url(#skyTone)" role="img" aria-label="Photo of a glass curtain wall tower"/>
    <polygon points="220,112 350,0 485,0 485,280" fill="url(#towerTone)" role="img" aria-label="Photo of installers setting a glass unit on a tower floor"/>
    <use href="#sheetFrame" width="485" height="686"/>
  </svg>
  <p class="brand-name">Fenwick</p>
  <div class="content" style="top:150px">
    <h2 class="title"><span class="accent">Brevanta</span>Solutions</h2>
    <ul class="points tight" style="margin-top:10px">
      <li>Curtain Wall</li><li>Ribbon Window</li>
      <li>Window Wall</li><li>Storefront</li>
    </ul>
    <p class="lead">Brevanta products can be installed in one third of the time with one third of the installers versus traditional stick products.</p>
    <ul class="points">
      <li>Enclose a building faster allowing other trades to start earlier</li>
      <li>Manufacturing done in a controlled environment</li>
      <li>Standard work and quality control inspections</li>
      <li>Less installers required</li>
    </ul>
  </div>
  <div class="contact-bar"><svg width="12" height="12"><use href="#phoneIcon"/></svg>555-014-2210<span class="divider"></span>555-014-2287</div>
  <span class="web">www.ktfenwickinc.com</span>
</article>

<!-- Flyer 2 -->
<article class="flyer f2">
  <svg class="flyer-art" viewBox="0 0 485 686" preserveAspectRatio="none">
    <rect width="485" height="686" fill="url(#sheetTone)" role="img" aria-label="Faded city skyline behind the text"/>
    <polygon points="0,115 70,0 330,0 140,175 0,280" fill="url(#skyTone)" role="img" aria-label="Photo of a tall glass office tower against the sky"/>
    <polygon points="220,112 350,0 485,0 485,280" fill="url(#towerTone)" role="img" aria-label="Photo of a gridded curtain wall building"/>
    <use href="#sheetFrame" width="485" height="686"/>
  </svg>
  <p class="brand-name">Fenwick</p>
  <div class="content" style="top:150px">
    <h2 class="title"><span class="accent">Brevanta</span>Curtain Wall</h2>
    <p class="lead">Designed by installers for installers with quality and efficient installation. Complete up to 40 panels a day with one installation team.</p>
    <ul class="points" style="row-gap:10px">
      <li>Industry leading 2 1/2” overall adjustment for out of tolerance structures</li>
      <li>Alignment pins allow for 1/4” forgiveness to engage units</li>
      <li>Trim clips and anchors are attached</li>
      <li>Shipped on metal racks or wood crates</li>
    </ul>
  </div>
  <div class="contact-bar"><svg width="12" height="12"><use href="#phoneIcon"/></svg>555-014-2210<span class="divider"></span>555-014-2287</div>
  <span class="web">www.ktfenwickinc.com</span>
</article>

<!-- Flyer 3 -->
<article class="flyer f3">
  <svg class="flyer-art" viewBox="0 0 485 686" preserveAspectRatio="none">
    <rect width="485" height="686" fill="url(#sheetTone)" role="img" aria-label="Faded city skyline behind the text"/>
    <polygon points="0,115 70,0 330,0 140,175 0,280" fill="url(#skyTone)" role="img" aria-label="Photo of a modern building with ribbon windows"/>
    <polygon points="220,112 350,0 485,0 485,280" fill="url(#towerTone)" role="img" aria-label="Photo of a white office building with storefront glazing"/>
    <use href="#sheetFrame" width="485" height="686"/>
  </svg>
  <p class="brand-name">Fenwick</p>
  <div class="content" style="top:152px">
    <h2 class="title compact"><span class="accent">Brevanta</span><span class="line">Ribbon Wall</span><span class="line">&amp; Storefront</span></h2>
    <p class="lead" style="margin-top:6px">Designed for quality and fast installation. This 2” by 4 1/2” system offers the following benefits:</p>
    <ul class="points tight">
      <li>Installed from the interior or exterior</li>
      <li>performance due to thermal strut</li>
      <li>Two color option (interior/exterior)</li>
      <li>Shipped on metal racks or wood crates</li>
      <li>Larger panes of glass to improve views</li>
      <li>12 psi water rating</li>
      <li>Higher thermal</li>
    </ul>
  </div>
  <div class="contact-bar"><svg width="12" height="12"><use href="#phoneIcon"/></svg>555-014-2210<span class="divider"></span>555-014-2287</div>
  <span class="web">www.ktfenwickinc.com</span>
</article>

<!-- Flyer 4 -->
<article class="flyer f4">
  <svg class="flyer-art" viewBox="0 0 485 686" preserveAspectRatio="none">
    <rect width="485" height="686" fill="url(#sheetTone)" role="img" aria-label="Faded city skyline behind the text"/>
    <polygon points="0,115 70,0 330,0 140,175 0,280" fill="url(#brickTone)" role="img" aria-label="Photo of a brick and glass residential building"/>
    <polygon points="220,112 350,0 485,0 485,280" fill="url(#towerTone)" role="img" aria-label="Photo of a high-rise residential tower"/>
    <use href="#sheetFrame" width="485" height="686"/>
  </svg>
  <p class="brand-name">Fenwick</p>
  <div class="content" style="left:12px;top:160px">
    <h2 class="title compact"><span class="accent" style="font-size:38px">Shipped On</span><span class="line">Metal Racks or</span><span class="line">Wood Crates</span></h2>
    <p class="lead" style="margin-top:8px">Designed by installers for an efficient installation with large vision areas. This 6” deep window system offers the following benefits:</p>
    <ul class="points" style="row-gap:4px">
      <li>Punched openings or window wall runs</li>
      <li>Trim clips are attached</li>
      <li>Shipped on metal racks or wood crates</li>
      <li>Metal slab covers</li>
      <li>Installed from the interior using a receptor system.</li>
    </ul>
  </div>
  <div class="contact-bar"><svg width="12" height="12"><use href="#phoneIcon"/></svg>555-014-2210<span class="divider"></span>555-014-2287</div>
  <span class="web">www.ktfenwickinc.com</span>
</article>

<!-- Flyer 5 -->
<article class="flyer f5">
  <svg class="flyer-art" viewBox="0 0 485 686" preserveAspectRatio="none">
    <rect width="485" height="686" fill="url(#sheetTone)" role="img" aria-label="Faded city skyline behind the text"/>
    <polygon points="0,115 70,0 330,0 140,175 0,280" fill="url(#shopTone)" role="img" aria-label="Photo of glass units stored in the factory"/>
    <polygon points="220,112 350,0 485,0 485,280" fill="url(#shopTone)" role="img" aria-label="Photo of the factory assembly floor"/>
    <use href="#sheetFrame" width="485" height="686"/>
  </svg>
  <p class="brand-name">Fenwick</p>
  <div class="content" style="top:154px">
    <h2 class="title"><span class="accent">Quality</span>Control</h2>
    <p class="subtitle">100% Factory Assembled</p>
    <ul class="points" style="margin-top:8px;row-gap:3px">
      <li>Temperature Controlled Clean Environment</li>
      <li>Lean Standard Work Training and Certification</li>
      <li>Sealant Manufacture Certification</li>
      <li>Rigorous Quality Inspections</li>
      <li>5% of Completed Units Tested for Air &amp; Water</li>
    </ul>
  </div>
  <div class="contact-bar"><svg width="12" height="12"><use href="#phoneIcon"/></svg>555-014-2210<span class="divider"></span>555-014-2287</div>
  <span class="web">www.ktfenwickinc.com</span>
</article>

<!-- Flyer 6 -->
<article class="flyer f6">
  <svg class="flyer-art" viewBox="0 0 485 686" preserveAspectRatio="none">
    <rect width="485" height="686" fill="url(#sheetTone)" role="img" aria-label="Faded city skyline behind the text"/>
    <polygon points="0,115 70,0 330,0 140,175 0,280" fill="url(#officeTone)" role="img" aria-label="Photo of a design team reviewing drawings at a screen"/>
    <polygon points="220,112 350,0 485,0 485,280" fill="url(#officeTone)" role="img" aria-label="Photo of engineers working at laptops in a meeting room"/>
    <use href="#sheetFrame" width="485" height="686"/>
  </svg>
  <p class="brand-name">Fenwick</p>
  <div class="content" style="left:19px;top:143px">
    <h2 class="title"><span class="accent">Design</span>Assist</h2>
    <p class="lead" style="margin:8px 0 6px">Through our Charrette Process, we work together with the entire team to identify the Owner's needs, the Architect's design intent, and the Contractor's schedule and budget.</p>
    <div class="tabs">
      <div>
        <h3 class="tab-head">Resources We Provide :</h3>
        <ul class="tab-list">
          <li>Curtain Wall Designer</li><li>Architect</li><li>Structural Engineer</li><li>Estimator</li><li>Project Manager</li>
        </ul>
      </div>
      <div>
        <h3 class="tab-head">Tools We Use:</h3>
        <ul class="tab-list">
          <li>Structra for BIM Models</li><li>Decision Matrix</li><li>Mind Map</li><li>Elevation Map</li><li>Document Tracking</li><li>Budget Updates</li><li>Product Samples</li>
        </ul>
      </div>
    </div>
  </div>
  <div class="contact-bar"><svg width="12" height="12"><use href="#phoneIcon"/></svg>555-014-2210<span class="divider"></span>555-014-2287</div>
  <span class="web">www.ktfenwickinc.com</span>
</article>

</body>
</html>
```